Broschüre für Immobilienmakler
Tolverido hat unsere Vorstellungen erkannt und von Beginn an super umgesetzt. Natürlich waren noch nachträgliche Änderungen und Feinabstimmungen notwendig. Diese wurden wunschgemäß perfektioniert. Man hatte hier wirklich sehr schöne Ideen in den Details ohne den Blick auf das Ganze zu verlieren. Dadurch haben wir jetzt eine perfekte Broschüre erhalten. Das war bestimmt nicht unser letztes Projekt. Vielen Dank
Zielgruppe
Wir sind Immobilienmakler & Home Stager; unsere hauptsächliche Zielgruppe sind Personen, die Ihre Immobilie verkaufen möchten. Die Broschüre soll ein wichtiger Teil der Akquise werden. Wir vermitteln als Immobilienmakler ganz ursprünglich, jedoch bieten wir auch den gesamten Service rund um den Verkauf (Einholung Unterlagen, Präsentieren der Immobilie durch kleine Effekte bis hin zu Entrümpelungen und Renovierung inkl. Einrichtungsbeispiele/Deko). Zudem sind wir jeden Tag (auch Sonn-und Feiertags) für unsere Kunden erreichbar und auch in Terminen. (Eindrücke gibt es auch über unsere Vombalo-Bewertungen)
Aufgabenstellung
Wir möchten einerseits natürlich mit unseren Vorzügen ggü. den 'Standard-Maklern' werben, aber auch genauso professionell den 'Standard-Dienst' ohne Home-Staging anbieten. (Viele Kunden denken schnell, dass wir nur außergewöhnliche und arbeitsintensive Objekte annehmen).
Texte würden wir versuchen zu übernehmen (hier würden wir die vorgesehenen Textfelder der Designer nutzen) und Bilder müssten vermutlich abgesprochen werden, da wir nicht sicher sind, ob unser Material dafür ausreicht. Die Bilder der Homepage liegen hier vor und können gerne zusätzlich gesendet werden.
Unsere Schriftart ist die Museo Sans rounded

```html
<!DOCTYPE html>
<html lang="de">
<head>
<meta charset="utf-8">
<title>Broschüre Hausglück – Immobilienmakler &amp; Home Stager</title>
<link href="https://fonts.googleapis.com/css2?family=Nunito:wght@400;600;700;800;900&display=swap" rel="stylesheet">
<style>
:root{
  --stage:#7d7d7d;
  --paper:#ffffff;
  --lilac:#a393bb;
  --lilac-dark:#8f7eaa;
  --ink:#1f1a22;
  --ink-soft:#3b3540;
  --rule:#b9aecb;
  --foot:#231c22;
}
*{margin:0;padding:0;box-sizing:border-box}
html,body{width:1200px;height:2317px;overflow:hidden}
body{background:var(--stage);font-family:"Nunito",sans-serif;color:var(--ink);position:relative}
.spread{position:absolute;left:40px;width:1120px;height:790px;background:var(--paper);overflow:hidden;border-bottom:10px solid var(--foot)}
.spread--outer{top:348px;border-top:5px solid var(--lilac)}
.spread--inner{top:1178px}
.abs{position:absolute}

/* outer spread */
.photo-house-faint{left:330px;top:40px;width:420px;height:420px;background:radial-gradient(ellipse at 50% 45%,#cfcfd2 0%,#e4e4e6 40%,rgba(255,255,255,0) 72%)}
.band{left:0;top:636px;width:1120px;height:144px;background:var(--lilac)}
.photo-team{left:150px;top:400px;width:330px;height:380px;background:radial-gradient(ellipse at 50% 55%,#6b6b6e 0%,#8d8d90 40%,rgba(160,160,165,0) 75%)}
.photo-house-hand{left:600px;top:380px;width:520px;height:400px;background:radial-gradient(ellipse at 40% 35%,#5a5f68 0%,#8b8f96 25%,rgba(222,195,178,.9) 45%,rgba(222,195,178,0) 70%)}

.brand-mini{left:48px;top:48px;width:120px;text-align:center}
.brand-mini .dot{display:block;width:58px;height:58px;margin:0 auto 10px;border-radius:50%;border:6px solid var(--lilac)}
.brand-mini .name{font-size:15px;font-weight:800;color:var(--lilac);letter-spacing:.5px}

.owners{left:182px;top:78px}
.owners .names{font-size:19px;font-weight:800;color:var(--lilac)}
.owners .role{font-size:12.5px;font-weight:800;color:var(--ink)}

.contact{left:127px;top:140px;width:300px;text-align:center;font-size:14.5px;line-height:1.2}
.contact .item{margin-bottom:20px}
.contact .ico{display:block;width:14px;height:14px;margin:0 auto 6px}
.contact .web{color:var(--lilac);font-weight:800}

.brand-main{left:745px;top:78px}
.brand-main .dot{position:absolute;left:0;top:0;width:92px;height:92px;border-radius:50%;border:9px solid var(--lilac)}
.brand-main .name{position:absolute;left:108px;top:30px;font-size:32px;font-weight:800;color:var(--ink);white-space:nowrap;letter-spacing:.5px}
.brand-main .tag{position:absolute;left:110px;top:72px;font-size:10px;font-weight:600;letter-spacing:1.2px;color:var(--ink-soft);white-space:nowrap}

.headline{left:600px;top:285px;width:490px;text-align:center;font-weight:900;font-size:23.5px;line-height:1.2;text-transform:uppercase}
.headline .plus{color:var(--lilac)}
.headline .city{display:block;color:var(--lilac)}

.perks{left:915px;top:385px;list-style:none;font-size:12.5px;font-weight:900;line-height:1.15;text-transform:uppercase}
.perks li{position:relative;padding-left:22px;margin-bottom:14px}
.tick::before,.perks li::before{content:"";position:absolute;left:0;top:2px;width:11px;height:11px;border-radius:50%;background:var(--lilac)}
.tick::after,.perks li::after{content:"";position:absolute;left:3.5px;top:4px;width:3px;height:5px;border:solid #fff;border-width:0 1.5px 1.5px 0;transform:rotate(45deg)}
.url-front{left:640px;top:724px;width:400px;text-align:center;color:#fff;font-weight:800;font-size:18.5px}

/* inner spread */
.photo-meeting{left:0;top:0;width:560px;height:270px;background:linear-gradient(180deg,#e2e2e4 0%,#cfcfd3 45%,#f0f0f1 80%,rgba(255,255,255,0) 100%)}
.section-tab{left:0;top:32px;width:354px;height:36px;background:var(--lilac);color:#fff;font-weight:900;font-size:19px;line-height:36px;text-align:center;clip-path:polygon(0 0,100% 0,96% 100%,0 100%)}
.col{top:285px}
.col--sale{left:54px;width:230px}
.col--rent{left:313px;width:212px}
.col-head{display:flex;align-items:center;margin-bottom:14px}
.col-head span{background:var(--lilac);color:#fff;font-weight:900;font-size:12px;padding:3px 14px 2px 12px;clip-path:polygon(0 0,100% 0,92% 100%,0 100%)}
.col-head i{flex:1;height:1.5px;background:var(--rule)}
.services{list-style:none;font-size:10.6px;line-height:1.15}
.services li{position:relative;padding-left:22px;margin-bottom:9.3px}
.services li.tick::before{top:1px}
.services li.tick::after{top:3px}
.col--rent .services li{margin-bottom:11.5px}
.sub-head{color:var(--lilac);font-weight:900;font-size:13px;line-height:1.05;margin:24px 0 11px}
.note{color:var(--lilac);font-weight:800;font-size:10.5px;line-height:1.15;margin-top:22px}
.col-rule{left:527px;top:295px;width:1.5px;height:470px;background:var(--rule)}

.gallery{left:585px;top:20px;display:grid;grid-template-columns:repeat(3,166px);grid-template-rows:repeat(3,166px);gap:7px}
.gallery .shot{width:166px;height:166px}
.gallery .label{background:var(--lilac);color:#fff;font-weight:900;font-size:19px;line-height:1.08;display:flex;align-items:center;justify-content:center;text-align:center}
.shot--living{background:linear-gradient(160deg,#6a5a4c,#e9e6e1 55%,#cfc8bf)}
.shot--hall{background:linear-gradient(180deg,#f3f2ef,#d9d4cc 60%,#5f6b3f)}
.shot--garden{background:linear-gradient(180deg,#5c7a3e,#86a35c 55%,#a99a86)}
.shot--attic{background:linear-gradient(150deg,#a47b53,#d7bb92 45%,#f1efe9)}
.shot--room{background:linear-gradient(180deg,#f4f3f1,#e8e5e0 55%,#c79a68)}
.shot--beams{background:linear-gradient(180deg,#3d2f27,#9b8c7e 40%,#f1efea)}
.shot--bath{background:linear-gradient(180deg,#efeeec,#d9dadd 50%,#f7f7f7)}
.shot--office{background:linear-gradient(160deg,#3a3836,#6d8a4c 40%,#b58a5c)}

.why{left:585px;top:555px;width:512px;display:flex;align-items:center;gap:14px}
.why i{flex:1;height:1.5px;background:var(--lilac)}
.why h2{font-size:19px;font-weight:900;color:var(--lilac);white-space:nowrap}
.quote{left:615px;top:588px;width:452px;text-align:center;font-size:10.8px;line-height:1.75;color:var(--ink-soft)}
.quote .mark{display:block;color:var(--lilac);font-weight:900;font-size:20px;line-height:1}
.url-tab{left:729px;top:722px;width:224px;height:58px;background:var(--lilac);color:#fff;font-weight:800;font-size:14px;display:flex;align-items:center;justify-content:center}
</style>
</head>
<body>

<section class="spread spread--outer" aria-label="Außenseite der Broschüre">
  <div class="abs photo-house-faint" role="img" aria-label="Blasses Foto eines Hausmodells auf offener Hand"></div>
  <div class="abs band"></div>
  <div class="abs photo-team" role="img" aria-label="Schwarzweiß-Porträt der beiden Makler mit verschränkten Armen"></div>
  <div class="abs photo-house-hand" role="img" aria-label="Hand hält ein kleines Hausmodell mit Schlüssel"></div>

  <div class="abs brand-mini"><span class="dot"></span><span class="name">HAUSGLÜCK</span></div>

  <div class="abs owners">
    <p class="names">Ilka &amp; Jonas Brevik</p>
    <p class="role">Immobilienmakler/in Home Stager/in (IHK)</p>
  </div>

  <div class="abs contact">
    <div class="item">
      <svg class="ico" viewBox="0 0 14 14"><circle cx="7" cy="7" r="7" fill="#a393bb"/><path d="M7 3a2.6 2.6 0 0 0-2.6 2.6C4.4 7.6 7 10.8 7 10.8s2.6-3.2 2.6-5.2A2.6 2.6 0 0 0 7 3z" fill="#fff"/><circle cx="7" cy="5.6" r="1" fill="#a393bb"/></svg>
      Lindenweg 14<br>42900 Ostbrunn
    </div>
    <div class="item">
      <svg class="ico" viewBox="0 0 14 14"><circle cx="7" cy="7" r="7" fill="#a393bb"/><path d="M4.4 3.6l1.4-.2.8 1.8-.9.7a5 5 0 0 0 2.4 2.4l.7-.9 1.8.8-.2 1.4c-3.4.4-6.4-2.6-6-6z" fill="#fff"/></svg>
      0123 – 45 67 890
    </div>
    <div class="item">
      <svg class="ico" viewBox="0 0 14 14"><circle cx="7" cy="7" r="7" fill="#a393bb"/><path d="M4.4 3.6l1.4-.2.8 1.8-.9.7a5 5 0 0 0 2.4 2.4l.7-.9 1.8.8-.2 1.4c-3.4.4-6.4-2.6-6-6z" fill="#fff"/></svg>
      0123 – 45 67 891
    </div>
    <div class="item">
      <svg class="ico" viewBox="0 0 14 14"><circle cx="7" cy="7" r="7" fill="#a393bb"/><rect x="3.6" y="4.6" width="6.8" height="4.8" fill="none" stroke="#fff" stroke-width="1"/><path d="M3.8 4.8L7 7.4l3.2-2.6" fill="none" stroke="#fff" stroke-width="1"/></svg>
      brevik@hausglueck.info
    </div>
    <div class="item web">
      <svg class="ico" viewBox="0 0 14 14"><circle cx="7" cy="7" r="7" fill="#a393bb"/><circle cx="7" cy="7" r="3.6" fill="none" stroke="#fff" stroke-width="1"/><path d="M3.4 7h7.2M7 3.4c-1.6 2-1.6 5.2 0 7.2M7 3.4c1.6 2 1.6 5.2 0 7.2" fill="none" stroke="#fff" stroke-width=".8"/></svg>
      www.hausglueck.info
    </div>
  </div>

  <div class="abs brand-main">
    <span class="dot"></span>
    <span class="name">HAUSGLÜCK</span>
    <span class="tag">DIE IMMOBILIENMAKLER</span>
  </div>

  <h1 class="abs headline">Immobilienmakler <span class="plus">+</span> Home Stager<span class="city">aus Ostbrunn</span></h1>

  <ul class="abs perks">
    <li>Kostenlose<br>Wertermittlung</li>
    <li>Kostenloser<br>Energieausweis<br>bei Verkauf</li>
    <li>Kostenlose<br>Erstberatung</li>
  </ul>

  <p class="abs url-front">www.hausglueck.info</p>
</section>

<section class="spread spread--inner" aria-label="Innenseite der Broschüre">
  <div class="abs photo-meeting" role="img" aria-label="Beratungsgespräch am Tisch mit Hausmodell und Händen"></div>
  <h2 class="abs section-tab">UNSERE LEISTUNGEN FÜR SIE:</h2>

  <div class="abs col col--sale">
    <div class="col-head"><span>VERKAUF:</span><i></i></div>
    <ul class="services">
      <li class="tick">Kostenlose Erstberatung</li>
      <li class="tick">Kostenlose Verkehrswertermittlung</li>
      <li class="tick">Kostenlose Erstellung eines<br>Energieausweises bei Verkauf</li>
      <li class="tick">Ansprechende professionelle Fotos</li>
      <li class="tick">Optionale Luftaufnahmen</li>
      <li class="tick">Besorgungen der notwendigen<br>Verkaufsunterlagen</li>
      <li class="tick">Objektaufbereitung</li>
      <li class="tick">Wettbewerbsanalyse</li>
      <li class="tick">Zielgruppenanalyse</li>
      <li class="tick">Werbe- und Marketingkonzept</li>
      <li class="tick">Flyer / Nachbarschaftswerbung<br>(auf Wunsch)</li>
      <li class="tick">Verkaufsschild (auf Wunsch)</li>
      <li class="tick">Besichtigungen / optional als<br>Open House inkl. Sektempfang</li>
      <li class="tick">Unterstützung und Betreuung</li>
      <li class="tick">Von der Beratung bis zur Übergabe</li>
      <li class="tick">Inserate in verschiedenen Medien</li>
      <li class="tick">Grundriss Erstellung (auf Wunsch)</li>
      <li class="tick">Sehr gute lokale Marktkenntnisse</li>
    </ul>
  </div>

  <div class="abs col col--rent">
    <div class="col-head"><span>VERMIETUNG:</span><i></i></div>
    <ul class="services">
      <li class="tick">Kostenlose Erstberatung</li>
      <li class="tick">Ansprechende<br>professionelle Fotos</li>
      <li class="tick">Unterstützung und Betreuung<br>von der Beratung bis zur<br>Übergabe</li>
      <li class="tick">Komplette Korrespondenz<br>mit Interessenten</li>
      <li class="tick">Inserate in<br>verschiedenen Medien</li>
      <li class="tick">Fertigung der Mietverträge</li>
    </ul>
    <h3 class="sub-head">Zusätzliche Leistungen<br>für den Verkauf:</h3>
    <ul class="services">
      <li class="tick">Home Staging</li>
      <li class="tick">Ausräumen der<br>Verkaufsimmobilie</li>
      <li class="tick">Renovierungsarbeiten</li>
      <li class="tick">Kleine Reparaturarbeiten</li>
      <li class="tick">Gartenpflege</li>
      <li class="tick">Grundreinigung</li>
    </ul>
    <p class="note">Zusätzlicher Service des Home<br>Staging ist möglich</p>
  </div>
  <div class="abs col-rule"></div>

  <div class="abs gallery">
    <div class="shot shot--living" role="img" aria-label="Helles Wohnzimmer mit Hängesessel"></div>
    <div class="shot shot--hall" role="img" aria-label="Flur mit Palme und Bilderwand"></div>
    <div class="shot shot--garden" role="img" aria-label="Gepflegter Garten mit Hecke"></div>
    <div class="shot shot--attic" role="img" aria-label="Dachgeschoss mit Holzdecke"></div>
    <div class="shot label">GALERIE<br>HOME<br>STAGING</div>
    <div class="shot shot--room" role="img" aria-label="Leerer Raum mit Holzboden und Teppich"></div>
    <div class="shot shot--beams" role="img" aria-label="Essbereich mit dunklen Deckenbalken"></div>
    <div class="shot shot--bath" role="img" aria-label="Helles Badezimmer mit Deckenleuchte"></div>
    <div class="shot shot--office" role="img" aria-label="Arbeitszimmer mit Schreibtisch und Pflanze"></div>
  </div>

  <div class="abs why"><i></i><h2>Warum Kunden auf uns setzen</h2><i></i></div>
  <blockquote class="abs quote">
    <span class="mark">“</span>
    Sehr professionelle Abwicklung. Wir hatten ein rundum Sorglospaket von der
    Firma Hausglück. Über ausräumen, kleinere Renovierungsarbeiten und
    geschmackvolle Einrichtung des Hauses haben sie die Immobilie innerhalb weniger
    Tage nach zahlreichen Anfragen erfolgreich verkauft. Der Kontakt war immer
    sehr nett. Super, machen sie weiter so.
    <span class="mark">”</span>
  </blockquote>
  <p class="abs url-tab">www.hausglueck.info</p>
</section>

</body>
</html>
```